Advert for Services that we offer

Bolt Remova Ltd need an design to represent what we do in a modern way by showing an image with a brief description and the use of corporate logo the information we will proved vie a doc file and this is to be presented in a modern way. This design will be for print & web. we have done our own design and its not great i have put this in the file repository

Target Market(s)

Motor trade

Font styles to use
Sans Serif

Colors

Designer to choose colors to be used in the design.

Requirements
Must have
• Company colour scheme as per logo within the files uploaded.
• and a small boarder to isolate it from the rest of the articles.
Nice to have
• Modern font
Should not have
• Old style font

```html
<!DOCTYPE html>
<html lang="en">
<head>
<meta charset="utf-8">
<title>Bolt Remova Ltd – Product Testing &amp; Analysis</title>
<link rel="stylesheet" href="https://fonts.googleapis.com/css2?family=Oswald:wght@600&family=Questrial&family=Open+Sans:wght@600;700&display=swap">
<style>
  :root {
    --brand-blue: #1f72bd;
    --ink: #2a2a2a;
    --text: #333333;
    --wedge-grey: #a7a8aa;
    --paper: #ffffff;
    --panel-top: #f1f2f4;
    --panel-bottom: #fbfbfc;
    --photo-dark: #3b4150;
    --photo-warm: #b5562e;
    --page-bg: #e9e9ea;
  }
  html, body {
    margin: 0;
    width: 1200px;
    height: 1200px;
    overflow: hidden;
    background: var(--page-bg);
  }
  .advert {
    position: absolute;
    left: 30px;
    top: 194px;
    width: 1314px;
    height: 936px;
    transform: scale(0.8676);
    transform-origin: top left;
    background: var(--paper);
  }
  .advert__panel {
    position: absolute;
    left: 12px; top: 11px; right: 12px; bottom: 7px;
    background: linear-gradient(180deg, var(--panel-top), var(--panel-bottom) 60%);
    overflow: hidden;
  }
  .advert__shapes {
    position: absolute;
    left: 0; top: 0;
    width: 1290px; height: 918px;
  }
  .headline {
    margin: 0;
    font-family: "Oswald", sans-serif;
    font-weight: 600;
    text-transform: uppercase;
  }
  .headline__line {
    position: absolute;
    right: 12px;
    font-size: 92px;
    line-height: 1;
    letter-spacing: -0.5px;
    white-space: nowrap;
    transform: scaleY(1.17);
    transform-origin: 100% 88px;
  }
  .headline__main { top: 30px; color: var(--brand-blue); }
  .headline__sub  { top: 147px; color: var(--ink); }
  .services {
    position: absolute;
    right: 42px;
    top: 318px;
    margin: 0;
    padding: 0;
    list-style: none;
    text-align: right;
    font-family: "Questrial", sans-serif;
    font-size: 44px;
    line-height: 46px;
    color: var(--text);
    white-space: nowrap;
  }
  .services li::after {
    content: "";
    display: inline-block;
    width: 6px; height: 6px;
    margin-left: 14px;
    border-radius: 50%;
    background: var(--brand-blue);
    vertical-align: middle;
  }
  .company {
    position: absolute;
    right: 30px;
    top: 705px;
    display: flex;
    align-items: center;
    gap: 16px;
    font-family: "Questrial", sans-serif;
    font-size: 44px;
    letter-spacing: 1px;
    color: var(--brand-blue);
    text-transform: uppercase;
    white-space: nowrap;
  }
  .company__mark {
    width: 26px; height: 26px;
    background: var(--brand-blue);
  }
  .contact {
    position: absolute;
    right: 38px;
    top: 808px;
    text-align: right;
    font-family: "Open Sans", sans-serif;
    color: #111;
    white-space: nowrap;
  }
  .contact__web { font-size: 33px; font-weight: 600; display: block; line-height: 44px; }
  .contact__phone { font-size: 28px; font-weight: 700; display: block; line-height: 38px; }
</style>
</head>
<body>
  <section class="advert" aria-label="Bolt Remova Ltd product testing advert">
    <div class="advert__panel">
      <svg class="advert__shapes" viewBox="0 0 1290 918">
        <defs>
          <linearGradient id="photoTone" x1="0" y1="0" x2="1" y2="1">
            <stop offset="0" stop-color="#3b4150"/>
            <stop offset="0.55" stop-color="#4a4f5c"/>
            <stop offset="1" stop-color="#b5562e"/>
          </linearGradient>
        </defs>
        <polygon class="wedge-grey" points="520,193 628,425 510,539 300,440" fill="#a7a8aa"/>
        <polygon class="wedge-blue" points="628,425 862,918 590,918 600,760 510,539" fill="#1f72bd"/>
        <polygon class="photo" role="img"
          aria-label="Photo: technician in safety glasses measuring a machined housing bore with a digital gauge"
          points="0,0 600,0 520,193 300,440 510,539 600,760 590,918 0,918" fill="url(#photoTone)"/>
      </svg>

      <h1 class="headline">
        <span class="headline__line headline__main">Product Testing</span>
        <span class="headline__line headline__sub">&amp; Analysis</span>
      </h1>

      <ul class="services">
        <li>Metallurgical testing</li>
        <li>Bearing pre-load testing</li>
        <li>Bore measurement</li>
        <li>New product evaluation</li>
        <li>Product analysis &amp; report</li>
      </ul>

      <div class="company">
        <span class="company__mark" aria-hidden="true"></span>
        <span class="company__name">Bolt Remova Ltd</span>
      </div>

      <div class="contact">
        <span class="contact__web">www.bolt-remova.co.uk</span>
        <span class="contact__phone">0161 496 0727</span>
      </div>
    </div>
  </section>
</body>
</html>
```